Brightmoor Law Letterhead for Law firm must be modern and use the logo I uploaded.

Hello I want a clean modern professional letterhead for my law firm Brightmoor Law. A logo has already been created and all files have been uploaded. The information for the firm can be given through message. Please use the logo that has already been created. Please also use the color scheme of that logo. (blue and white).

Target Market(s)

General Public

Industry/Entity Type

Law Firm

Colors

Designer to choose colors to be used in the design.

Requirements
Must have
• This must be a modern professional letterhead
Nice to have
• My logo that is included in file form
Should not have
• Should not have logo that is not the one I uploaded.

```html
<!DOCTYPE html>
<html lang="en">
<head>
<meta charset="UTF-8">
<title>Brightmoor Law Letterhead</title>
<link href="https://fonts.googleapis.com/css2?family=Roboto:wght@400;500;700&display=swap" rel="stylesheet">
<style>
  :root {
    --navy: #2e3262;
    --frame: #c9c9d8;
    --backdrop: #e6e6e6;
    --paper: #ffffff;
    --ink: #1a1a1a;
  }
  * { margin: 0; padding: 0; box-sizing: border-box; }
  html, body {
    width: 1150px;
    height: 1200px;
    overflow: hidden;
    background: var(--backdrop);
    font-family: "Roboto", sans-serif;
    color: var(--ink);
  }
  .letterhead {
    position: absolute;
    left: 190px;
    top: 102px;
    width: 770px;
    height: 995px;
    background: var(--paper);
  }
  .frame {
    position: absolute;
    left: 65px;
    top: 73px;
    width: 642px;
    height: 850px;
    border: 2px solid var(--frame);
    border-top: none;
  }
  .frame-top {
    position: absolute;
    top: 73px;
    height: 2px;
    background: var(--frame);
  }
  .frame-top.left { left: 65px; width: 169px; }
  .frame-top.right { left: 537px; width: 170px; }
  .brand-block {
    position: absolute;
    left: 268px;
    top: 0;
    width: 233px;
    height: 161px;
    background: var(--navy);
    display: flex;
    align-items: center;
    justify-content: center;
  }
  .brand-name {
    color: #ffffff;
    font-weight: 500;
    font-size: 15px;
    letter-spacing: 0.32em;
    margin-right: -0.32em;
    text-transform: uppercase;
  }
  .addressee {
    position: absolute;
    right: 118px;
    top: 223px;
    text-align: right;
    font-size: 13.5px;
    line-height: 20px;
  }
  .addressee .date { margin-bottom: 10px; }
  .addressee .name { font-weight: 700; }
  .letter-body {
    position: absolute;
    left: 136px;
    top: 478px;
    width: 516px;
    font-size: 13.5px;
    line-height: 25px;
    text-align: justify;
  }
  .letter-body p + p { margin-top: 25px; }
  .contact-bar {
    position: absolute;
    left: 65px;
    top: 938px;
    width: 642px;
    height: 20px;
    font-size: 11.7px;
    color: var(--navy);
  }
  .contact-item {
    position: absolute;
    top: 0;
    display: flex;
    align-items: center;
    gap: 8px;
    white-space: nowrap;
  }
  .contact-item svg { width: 14px; height: 14px; fill: var(--navy); }
  .contact-item.address { left: 0; }
  .contact-item.phone { left: 320px; }
  .contact-item.web { right: 0; }
  .base-band {
    position: absolute;
    left: 0;
    bottom: 0;
    width: 100%;
    height: 29px;
    background: var(--navy);
  }
</style>
</head>
<body>
  <main class="letterhead">
    <div class="frame"></div>
    <div class="frame-top left"></div>
    <div class="frame-top right"></div>

    <header class="brand-block">
      <span class="brand-name">Brightmoor Law</span>
    </header>

    <section class="addressee">
      <p class="date">November 16, 2023</p>
      <p class="name">Recippient Name</p>
      <p>Vice President</p>
      <p>Example Incooration</p>
      <p>State</p>
    </section>

    <article class="letter-body">
      <p>Lorem ipsum dolor sit amet, consectetur adipiscing elit. Phasellus nec velit sed ligula facilisis malesuada interdum non urna. Aliquam auctor eros sed gravida viverra. Mauris fringilla ac elit vitae laoreet. Integer condimentum vel lectus non eleifend. Quisque facilisis faucibus blandit. Proin vestibulum dapibus ipsum eu commodo. Nullam hendrerit lectus nec lectus venenatis mattis.</p>
      <p>Vestibulum ornare lorem sed feugiat faucibus. Morbi efficitur sapien ut tellus pellentesque, a lacinia nisi fermentum. Sed viverra mi lacus, ac scelerisque nisl fringilla at. Nullam lectus ipsum, laoreet ac libero eget, dapibus faucibus magna. Orci varius natoque penatibus et magnis dis parturient montes, nascetur ridiculus mus. Integer in posuere orci. Pellentesque euismod ut ante eu elementum. Ut consectetur ac urna sed varius. Aliquam consectetur tortor erat, non aliquet libero accumsan id.</p>
      <p>Nunc magna purus, fermentum ut nulla vitae, aliquet placerat urna. Donec leo justo, ornare quis lectus sit amet, aliquam venenatis diam. Vivamus pharetra dui ut quam sagittis dignissim. Aliquam eget turpis purus. Aliquam erat volutpat. Etiam sed ultricies purus, bibendum porttitor neque.</p>
    </article>

    <footer class="contact-bar">
      <div class="contact-item address">
        <svg viewBox="0 0 24 24" aria-hidden="true"><path d="M12 1a9 9 0 0 0-9 9c0 6.5 9 13 9 13s9-6.5 9-13a9 9 0 0 0-9-9zm0 5a4 4 0 1 1 0 8 4 4 0 0 1 0-8z"/></svg>
        <span>NAME OF STREET, CITY, PROVINCE, COUNTRY</span>
      </div>
      <div class="contact-item phone">
        <svg viewBox="0 0 24 24" aria-hidden="true"><circle cx="12" cy="12" r="12"/><path fill="#fff" d="M8.6 6.2l1.8 2.6-1.2 1.3c.8 1.7 2 2.9 3.7 3.7l1.3-1.2 2.6 1.8-.9 2.1c-4.6-.5-8.1-4-8.6-8.6z"/></svg>
        <span>00 123 456 789</span>
      </div>
      <div class="contact-item web">
        <svg viewBox="0 0 24 24" aria-hidden="true"><path d="M12 1a11 11 0 1 0 0 22 11 11 0 0 0 0-22zm0 2c1.3 0 2.7 2.5 3.2 6H8.8C9.3 5.5 10.7 3 12 3zM3.2 11h3.5c0 .7 0 1.3.1 2H3.2a9 9 0 0 1 0-2zm5.5 0h6.6a17 17 0 0 1 0 2H8.7a17 17 0 0 1 0-2zm8.6 0h3.5a9 9 0 0 1 0 2h-3.5c.1-.7.1-1.3 0-2zM12 21c-1.3 0-2.7-2.5-3.2-6h6.4c-.5 3.5-1.9 6-3.2 6z"/></svg>
        <span>WWW.BRIGHTMOORLAW.COM</span>
      </div>
    </footer>

    <div class="base-band"></div>
  </main>
</body>
</html>
```